Formal letterhead for Commercial Real Estate Company

Formal and professional letterhead for the transactional documents of a commercial real estate company.

Elements to be Included between header and footer:

- Logo (attached)(should be applied without the yellow background, in other words, the background colour for the design should be white)
- Slogan: Your Property Solution
- Physical Address: 41 Tennant Lane, Oakridge, Durban, 4001
- Postal Address: PO Box 72814, Fernhill, 4062
- Phone: 031 648 9125
- Fax: 031 573 4189
- Website: www.delvane.co.zaz
- eMail: contact@delvane.co.za

The brand guide is attached (the one you last provided), it does not provide direction on letterhead specifically but on other brand aspects.

Industry/Entity Type

Real Estate

```html
<!DOCTYPE html>
<html lang="en">
<head>
<meta charset="utf-8">
<title>Delvane Letterhead</title>
<link href="https://fonts.googleapis.com/css2?family=Open+Sans:wght@400;700&display=swap" rel="stylesheet">
<style>
  :root {
    --ink: #111111;
    --paper: #ffffff;
    --backdrop: #9a9a9a;
    --muted: #333333;
  }
  html, body {
    margin: 0;
    padding: 0;
    width: 1079px;
    height: 1200px;
    overflow: hidden;
    background: var(--backdrop);
    font-family: "Open Sans", Arial, sans-serif;
  }
  .letterhead {
    position: absolute;
    left: 115px;
    top: 0;
    width: 849px;
    height: 1200px;
    background: var(--paper);
  }
  .header-band {
    position: absolute;
    left: 0;
    right: 0;
    top: 196px;
    height: 34px;
    background: var(--ink);
  }
  .brand {
    position: absolute;
    left: 50%;
    top: 172px;
    transform: translateX(-50%);
    width: 190px;
    height: 80px;
    background: var(--paper);
    display: flex;
    align-items: center;
    justify-content: center;
    gap: 10px;
  }
  .brand-mark {
    width: 16px;
    height: 16px;
    background: var(--ink);
  }
  .brand-name {
    font-weight: 700;
    font-size: 34px;
    color: var(--ink);
    letter-spacing: 0.5px;
  }
  .footer-rule {
    position: absolute;
    left: 0;
    right: 0;
    background: var(--ink);
  }
  .footer-rule.top { top: 1022px; height: 4px; }
  .footer-rule.bottom { top: 1142px; height: 6px; }
  .contact {
    position: absolute;
    right: 56px;
    top: 1046px;
    text-align: right;
    font-size: 12px;
    line-height: 19px;
    color: var(--muted);
  }
  .contact-line { white-space: nowrap; }
  .contact-item {
    display: inline-flex;
    align-items: center;
    gap: 4px;
  }
  .contact-item svg { width: 10px; height: 10px; }
  .sep { margin: 0 5px; }
  .slogan {
    position: absolute;
    right: 56px;
    top: 1102px;
    font-size: 12px;
    font-weight: 700;
    letter-spacing: 5px;
    color: var(--ink);
    text-transform: uppercase;
  }
</style>
</head>
<body>
  <main class="letterhead">
    <div class="header-band"></div>
    <div class="brand">
      <span class="brand-mark"></span>
      <span class="brand-name">Delvane</span>
    </div>

    <div class="footer-rule top"></div>

    <address class="contact" style="font-style:normal">
      <div class="contact-line">41 Tennant Lane, Oakridge, Durban, 4001<span class="sep">|</span>PO Box 72814, Fernhill, 4062</div>
      <div class="contact-line">
        <span class="contact-item">
          <svg viewBox="0 0 10 10" aria-hidden="true"><path d="M2 1 L4 3 L3 4 Q4 6 6 7 L7 6 L9 8 L8 9.5 Q3 9 0.5 2 Z" fill="#333"/></svg>031 648 9125</span><span class="sep">|</span>
        <span class="contact-item">
          <svg viewBox="0 0 10 10" aria-hidden="true"><rect x="1" y="3" width="8" height="5" rx="1" fill="#333"/><rect x="3" y="1" width="4" height="2" fill="#333"/></svg>031 573 4189</span><span class="sep">|</span>
        <span class="contact-item">
          <svg viewBox="0 0 10 10" aria-hidden="true"><rect x="0.5" y="2" width="9" height="6" fill="#333"/><path d="M0.5 2 L5 5.5 L9.5 2" stroke="#fff" stroke-width="1" fill="none"/></svg>contact@delvane.co.za</span><span class="sep">|</span>
        <span class="contact-item">
          <svg viewBox="0 0 10 10" aria-hidden="true"><circle cx="5" cy="5" r="4.3" fill="none" stroke="#333" stroke-width="1.2"/><path d="M0.7 5 H9.3 M5 0.7 Q2.5 5 5 9.3 M5 0.7 Q7.5 5 5 9.3" stroke="#333" stroke-width="0.8" fill="none"/></svg>www.delvane.co.zaz</span>
      </div>
    </address>

    <div class="slogan">Your Property Solution</div>

    <div class="footer-rule bottom"></div>
  </main>
</body>
</html>
```